Creative designs Needed! Dieting Tips for Nurses

Need a creative design for my first book that is targeted to nurses that want to lose weight.
THE TITLE OF MY BOOK IS:
The Bright Lantern Pantry Uprising:
9 Slim-Down Tricks Each Caregiver Should Learn!

- My audience is female.

- My colors for my business are red, black, gray and white however feel free to use other colors

- The cover should note there is Free Bonus Content.

- The book cover should have a fun modern feel to it.

- Since the title is talking about time. I think there should be some sort of clock in the design. Not an actual clock but a clock design.

- Please let me know if you need anything from me to complete your design. I go by Coach Brin.

- Subject of book is dieting tips for nurses

Target Market(s)

Nurses

Industry/Entity Type

Health And Wellness

Font styles to use
Serif

Colors
ec1f27
1b1b1b
dddddd

Requirements
Must have
• List the Free Bonus Content label on the front cover
• Must keep in mind there will be sequels to this book for other target markets
• • Should be creative, modern
• • Please try not to use stock images with just the text for this design - I am looking for something creative and unique.
• • Something that plays with the idea of time, think clock.
• • Need something out the box!!
• • Think diversity in the people if you do opt to use images - Would prefer if you steer clear of regular photos of people
• • If you do use an image of a nurse, please note nurses mostly wear scrubs today - so think about that in your concepts
Nice to have
• The design should be clever
Should not have
• Although I selected the 3 colors feel free to explore other colors and those 3 colors do not have to be the dominate colors.
• The book design should pop out to people when they see it.

```html
<!DOCTYPE html>
<html lang="en">
<head>
<meta charset="utf-8">
<title>The Bright Lantern Pantry Uprising – Book Cover</title>
<link rel="stylesheet" href="https://fonts.googleapis.com/css2?family=Tinos:wght@400;700&display=swap">
<style>
  :root {
    --red: #ec1f27;
    --ink: #1b1b1b;
    --white: #ffffff;
    --grey: #dddddd;
    --skin-light: #f3e6dc;
    --skin: #e7c9b4;
    --skin-deep: #dcb39b;
    --shorts: #a9dde6;
    --backdrop: #cfeef2;
    --band: rgba(255, 255, 255, 0.9);
  }
  html, body {
    margin: 0;
    padding: 0;
    width: 800px;
    height: 1200px;
    overflow: hidden;
  }
  .cover {
    position: relative;
    width: 800px;
    height: 1200px;
    overflow: hidden;
    font-family: "Tinos", "Times New Roman", serif;
    color: var(--ink);
  }
  .cover-photo {
    position: absolute;
    inset: 0;
    background:
      radial-gradient(ellipse 40% 45% at 92% 40%, rgba(207, 238, 242, 0.95), transparent 70%),
      radial-gradient(ellipse 60% 30% at 40% 45%, rgba(220, 179, 155, 0.55), transparent 75%),
      linear-gradient(180deg, var(--skin-light) 0%, var(--skin) 28%, var(--skin-deep) 52%, var(--shorts) 62%, #b8e3ea 80%, var(--backdrop) 100%);
  }
  .clock-ring {
    position: absolute;
    left: 130px;
    top: 300px;
    width: 540px;
    height: 540px;
  }
  .title-tag {
    position: absolute;
    background: var(--red);
    color: var(--white);
    font-weight: 400;
    line-height: 1;
    padding: 3px 8px 2px;
  }
  .title-tag--top {
    left: 114px;
    top: 74px;
    font-size: 36px;
    letter-spacing: 5px;
  }
  .title-main {
    position: absolute;
    left: 116px;
    top: 132px;
    margin: 0;
    font-size: 40px;
    font-weight: 400;
    letter-spacing: 3.5px;
    line-height: 1;
    white-space: nowrap;
  }
  .title-tag--bottom {
    right: 118px;
    top: 192px;
    font-size: 36px;
    letter-spacing: 5px;
  }
  .bonus-badge {
    position: absolute;
    left: 566px;
    top: 690px;
    width: 168px;
    height: 168px;
    border-radius: 50%;
    background: var(--red);
    color: var(--white);
    border: 4px solid var(--white);
    box-sizing: border-box;
    display: flex;
    flex-direction: column;
    align-items: center;
    justify-content: center;
    text-align: center;
    text-transform: uppercase;
    line-height: 1.05;
  }
  .bonus-badge__free {
    font-size: 34px;
    font-weight: 700;
    letter-spacing: 2px;
  }
  .bonus-badge__label {
    font-size: 19px;
    letter-spacing: 1.5px;
    margin-top: 4px;
  }
  .subtitle-band {
    position: absolute;
    left: 0;
    top: 916px;
    width: 800px;
    height: 138px;
    background: linear-gradient(90deg, var(--band) 0%, var(--band) 72%, rgba(255,255,255,0.55) 90%, transparent 100%);
  }
  .subtitle-band::before,
  .subtitle-band::after {
    content: "";
    position: absolute;
    left: 0;
    width: 100%;
    height: 9px;
    background: linear-gradient(90deg, transparent 0%, var(--red) 10%, var(--red) 76%, transparent 100%);
  }
  .subtitle-band::before { top: 0; }
  .subtitle-band::after { bottom: 0; }
  .subtitle {
    position: absolute;
    left: 0;
    width: 800px;
    top: 32px;
    margin: 0;
    text-align: center;
    font-size: 33px;
    font-weight: 400;
    letter-spacing: 2px;
    line-height: 40px;
    text-transform: uppercase;
  }
  .author {
    position: absolute;
    left: 40px;
    top: 1098px;
    font-size: 50px;
    font-weight: 700;
    color: var(--red);
    line-height: 1;
  }
</style>
</head>
<body>
  <main class="cover">
    <div class="cover-photo" role="img" aria-label="Photo of a woman's slim waist in light blue shorts, hands wrapping a yellow measuring tape around it"></div>

    <svg class="clock-ring" viewBox="0 0 540 540" aria-hidden="true">
      <circle cx="270" cy="270" r="255" fill="none" stroke="#ffffff" stroke-opacity="0.7" stroke-width="4"/>
      <circle cx="270" cy="270" r="240" fill="none" stroke="#ffffff" stroke-opacity="0.35" stroke-width="1.5"/>
      <g stroke="#ffffff" stroke-opacity="0.85" stroke-width="5" stroke-linecap="round">
        <line x1="270" y1="22" x2="270" y2="52"/>
        <line x1="518" y1="270" x2="488" y2="270"/>
        <line x1="270" y1="518" x2="270" y2="488"/>
        <line x1="22" y1="270" x2="52" y2="270"/>
      </g>
      <g stroke="#ffffff" stroke-opacity="0.7" stroke-width="3" stroke-linecap="round">
        <line x1="394" y1="55" x2="386" y2="69"/>
        <line x1="485" y1="146" x2="471" y2="154"/>
        <line x1="485" y1="394" x2="471" y2="386"/>
        <line x1="394" y1="485" x2="386" y2="471"/>
        <line x1="146" y1="485" x2="154" y2="471"/>
        <line x1="55" y1="394" x2="69" y2="386"/>
        <line x1="55" y1="146" x2="69" y2="154"/>
        <line x1="146" y1="55" x2="154" y2="69"/>
      </g>
      <g stroke="#ec1f27" stroke-width="6" stroke-linecap="round">
        <line x1="270" y1="270" x2="270" y2="110"/>
        <line x1="270" y1="270" x2="380" y2="270"/>
      </g>
      <circle cx="270" cy="270" r="10" fill="#ec1f27"/>
    </svg>

    <span class="title-tag title-tag--top">THE</span>
    <h1 class="title-main">BRIGHT LANTERN PANTRY</h1>
    <span class="title-tag title-tag--bottom">UPRISING</span>

    <div class="bonus-badge">
      <span class="bonus-badge__free">Free</span>
      <span class="bonus-badge__label">Bonus<br>Content</span>
    </div>

    <section class="subtitle-band">
      <p class="subtitle">9 Slim-Down Tricks Each<br>Caregiver Should Learn!</p>
    </section>

    <div class="author">Coach Brin</div>
  </main>
</body>
</html>
```